Keel Harbor Windows & Doors

We are an aluminum windows & doors manufacturer. Need a professional & vision appealing web design. It should reflects our professional business character, but with very user-friendly interface( catch eyes, use simple icon or symbol to make it easy to read...) Don't copy : ) but can use some competitor's web (https://www.brimfordglazing.example) (www.qelmoframes.example) to have a glance on our target and web content as reference

Target Market(s)

Homeowner and Professional (Builder / Developer/ Architect & window installer)

Industry/Entity Type

Manufacturer

Font styles to use
Serif
Sans Serif

Requirements
Must have
• Have 3 serials products. Residential (value for money) Commercial (Professional and quality) Architectural (Bold & funky)
• Color match or harmony with the selected logo design
Nice to have
• Project gallery display, have online free quote to upload files, can insert video or cartoon
Should not have
• no limitation on your imagination ; )

```html
<!DOCTYPE html>
<html lang="en">
<head>
<meta charset="utf-8">
<title>Keel Harbor Windows & Doors</title>
<link href="https://fonts.googleapis.com/css2?family=Roboto+Condensed:wght@400;700&family=Open+Sans:ital,wght@0,400;0,600;1,400&display=swap" rel="stylesheet">
<style>
:root{
  --green:#7cc242;
  --green-dark:#69a935;
  --ink:#2b2b2b;
  --text:#555;
  --grey:#8c8c8c;
  --light:#f3f3f3;
  --dark:#1f2326;
  --white:#fff;
}
*{margin:0;padding:0;box-sizing:border-box}
html,body{width:1200px;height:3093px;overflow:hidden}
body{position:relative;background:var(--white);font-family:"Open Sans",Arial,sans-serif;color:var(--text)}
.abs{position:absolute}
.head-font{font-family:"Roboto Condensed","Arial Narrow",sans-serif}

/* header */
.site-header{left:0;top:0;width:1200px;height:165px;background:var(--light)}
.brand{left:97px;top:40px;display:flex;align-items:center;gap:14px}
.brand-mark{width:34px;height:34px;background:var(--green)}
.brand-name{font-family:"Roboto Condensed",sans-serif;font-weight:700;font-size:34px;color:var(--green);letter-spacing:1px}
.contact-top{left:650px;top:32px;display:flex;gap:14px;align-items:center;font-size:16px;color:#444;line-height:21px}
.contact-top .ico{width:36px;height:36px;border-radius:50%;background:#777;display:flex;align-items:center;justify-content:center}
.btn-quote-top{left:950px;top:35px;width:150px;height:34px;border-radius:17px;background:var(--green);color:#fff;font:400 13px "Roboto Condensed",sans-serif;display:flex;align-items:center;justify-content:center}
.main-nav{left:360px;top:115px;width:740px;height:50px;display:flex}
.main-nav .home{width:85px;background:linear-gradient(100deg,transparent 0 18px,#8d8d8d 18px);color:#fff;padding-left:30px}
.main-nav .rest{flex:1;background:var(--green);display:flex;justify-content:space-around;padding:0 10px}
.main-nav a{font:400 13.5px "Roboto Condensed",sans-serif;color:#fff;text-decoration:none;display:flex;align-items:center}

/* hero */
.hero{left:0;top:165px;width:1200px;height:518px;background:linear-gradient(180deg,#5d6266 0%,#3b4045 45%,#2a2d30 100%)}
.hero-photo{left:0;top:0;width:1200px;height:518px;background:radial-gradient(ellipse at 55% 40%,rgba(150,160,165,.45),transparent 60%)}
.hero-title{left:97px;top:152px;font:700 44px/46px "Roboto Condensed",sans-serif;color:#fff}
.hero-text{left:97px;top:260px;width:350px;font-size:13px;line-height:19px;color:#eee}
.btn-green{background:var(--green);color:#fff;font:400 14px "Roboto Condensed",sans-serif;display:flex;align-items:center;justify-content:center}
.hero-btn{left:97px;top:318px;width:113px;height:32px}
.arrow{width:34px;height:34px;border-radius:50%;background:#1e1e1e;top:243px}
.quote-panel{left:783px;top:78px;width:317px;height:375px;background:rgba(20,22,24,.78);border:1px solid rgba(255,255,255,.15);padding:22px 27px}
.quote-panel h2{font:400 24px "Roboto Condensed",sans-serif;color:#fff;text-align:center;margin-bottom:18px}
.field{height:44px;background:#fff;border-radius:3px;margin-bottom:11px;font-size:11px;color:#888;padding:13px 12px}
.field.msg{height:44px}
.quote-submit{margin:16px auto 0;width:170px;height:34px;border-radius:3px}

/* welcome */
.video-box{left:100px;top:773px;width:463px;height:287px;border:4px solid #e5e5e5;background:linear-gradient(90deg,#cfd3d2 0%,#3a4146 40%,#6f7b80 55%,#b7c4c8 100%)}
.play{left:216px;top:125px;width:30px;height:26px;background:#111;border-radius:3px}
.welcome-title{left:598px;top:782px;font:400 36px "Roboto Condensed",sans-serif;color:var(--ink)}
.welcome-title span{color:var(--green)}
.welcome-text{left:598px;top:840px;width:505px;font-size:11.5px;line-height:21px;color:#666}
.btn-grey{left:598px;top:1008px;width:104px;height:32px;background:#8c8c8c;color:#fff;font:400 12px "Roboto Condensed",sans-serif;display:flex;align-items:center;justify-content:center;border-radius:2px}

/* products */
.products{left:0;top:1150px;width:1200px;height:547px;background:linear-gradient(180deg,rgba(124,194,66,.93),rgba(124,194,66,.95)),linear-gradient(180deg,#9aa 0,#566 100%)}
.section-title{width:1200px;left:0;text-align:center;font:700 32px "Roboto Condensed",sans-serif}
.products .section-title{top:92px;color:#fff}
.dash-line{left:243px;top:247px;width:715px;border-top:2px dashed rgba(255,255,255,.7)}
.product{top:190px;width:300px;text-align:center;color:#fff}
.diamond{width:82px;height:82px;margin:30px auto 0;transform:rotate(45deg);background:var(--grey);border:3px solid #fff;display:flex;align-items:center;justify-content:center}
.diamond svg{transform:rotate(-45deg)}
.product h3{margin-top:48px;font:700 21px "Roboto Condensed",sans-serif}
.product p{margin-top:10px;font-size:11px;line-height:17px;padding:0 10px}
.product a{display:block;margin-top:18px;font-size:11px;color:#fff;text-decoration:underline}

/* gallery */
.gallery .section-title{top:1760px;color:var(--ink)}
.tile{position:absolute}
.tile-caption{position:absolute;inset:12px;background:rgba(124,194,66,.85);border:3px solid rgba(255,255,255,.4);display:flex;flex-direction:column;align-items:center;justify-content:center;color:#fff;font-size:14px;text-align:center;line-height:20px}

/* testimonials */
.testimonials{left:0;top:2388px;width:1200px;height:352px;background:linear-gradient(180deg,#2c3033,#1b1e20)}
.testimonials .section-title{top:68px;color:#fff}
.rule{left:560px;top:118px;width:80px;height:2px;background:#fff}
.quote{left:195px;top:148px;width:810px;text-align:center;font-style:italic;font-size:12px;line-height:21px;color:#ddd}
.author{left:0;top:228px;width:1200px;text-align:center;font-style:italic;font-size:13.5px;color:#fff}
.dots{left:558px;top:278px;display:flex;gap:6px}
.dots i{width:25px;height:3px;background:#777}
.dots i:first-child{background:#fff}

/* footer */
.site-footer{left:0;top:2740px;width:1200px;height:295px;background:#f1f1f1}
.foot-col h4{font:400 22px "Roboto Condensed",sans-serif;color:#333;margin-bottom:16px}
.foot-col{top:50px;font-size:12px;color:#555;line-height:20px}
.foot-row{display:flex;gap:14px;margin-bottom:12px}
.newsletter-input{width:245px;height:40px;background:#fff;border:1px solid #e2e2e2;margin-top:14px;padding:11px 12px;font-size:11px;color:#777}
.btn-signup{width:122px;height:36px;margin-top:15px}
.links li{list-style:none;padding-left:18px;position:relative;line-height:20.5px}
.links li::before{content:"›";position:absolute;left:2px;color:#888}
.foot-brand{left:920px;top:100px;display:flex;align-items:center;gap:10px}
.foot-brand .brand-name{font-size:26px}
.socials{left:963px;top:2926px;display:flex;gap:6px}
.socials i{width:22px;height:22px;border-radius:50%;border:1px solid #777}
.copyright{left:0;top:3035px;width:1200px;height:58px;background:#fff;border-top:1px solid #ddd;text-align:center;font-size:11px;color:#555;padding-top:23px}
</style>
</head>
<body>

<header class="site-header abs">
  <div class="brand abs"><span class="brand-mark"></span><span class="brand-name">KEEL HARBOR</span></div>
  <div class="contact-top abs">
    <span class="ico"><svg width="18" height="18" viewBox="0 0 24 24"><path fill="#fff" d="M6.6 10.8a15 15 0 0 0 6.6 6.6l2.2-2.2c.3-.3.7-.4 1-.2 1.1.4 2.3.6 3.6.6.6 0 1 .4 1 1V20c0 .6-.4 1-1 1A17 17 0 0 1 3 4c0-.6.4-1 1-1h3.5c.6 0 1 .4 1 1 0 1.3.2 2.5.6 3.6.1.3 0 .7-.2 1z"/></svg></span>
    <div>Call Us: (09) 5550 1427<br>info@keelharbor.example</div>
  </div>
  <div class="btn-quote-top abs">ONLINE FREE QUOTE</div>
  <nav class="main-nav abs">
    <a class="home">HOME</a>
    <div class="rest">
      <a>ABOUT US</a><a>OUR PRODUCTS</a><a>OUR PROJECTS</a><a>FABRICATORS</a><a>BLOG</a><a>CONTACT US</a>
    </div>
  </nav>
</header>

<section class="hero abs">
  <div class="hero-photo abs" role="img" aria-label="Modern glass-fronted office building at dusk"></div>
  <h1 class="hero-title abs">KEEL HARBOR<br>WINDOWS &amp; DOORS</h1>
  <p class="hero-text abs">Nemo enim ipsam voluptatem quia voluptas sit aspernatur aut odit aut fugit, sed quia</p>
  <div class="hero-btn btn-green abs">READ MORE</div>
  <div class="arrow abs" style="left:33px"><svg width="34" height="34"><path d="M20 11l-6 6 6 6" stroke="#fff" stroke-width="2" fill="none"/></svg></div>
  <div class="arrow abs" style="left:1130px"><svg width="34" height="34"><path d="M14 11l6 6-6 6" stroke="#fff" stroke-width="2" fill="none"/></svg></div>
  <form class="quote-panel abs">
    <h2>ONLINE FREE QUOTE</h2>
    <div class="field">Name *</div>
    <div class="field">Mobile phone *</div>
    <div class="field">Email *</div>
    <div class="field msg">Message *</div>
    <div class="quote-submit btn-green">ONLINE FREE QUOTE</div>
  </form>
</section>

<section class="welcome">
  <div class="video-box abs" role="img" aria-label="Close-up of an aluminium sliding door frame">
    <div class="play abs"><svg width="30" height="26"><path d="M12 8l8 5-8 5z" fill="#fff"/></svg></div>
  </div>
  <h2 class="welcome-title abs">WELCOME TO <span>KEEL HARBOR</span></h2>
  <div class="welcome-text abs">
    <p>Sed ut perspiciatis unde omnis iste natus error sit voluptatem accusantium doloremque laudantium, totam rem aperiam, eaque ipsa quae ab illo inventore veritatis et quasi architecto beatae vitae dicta sunt explicabo. Nemo enim ipsam voluptatem quia voluptas sit aspernatur aut odit aut fugit, sed quia consequuntur magni dolores eos qui ratione</p>
    <p style="margin-top:10px">Nemo enim ipsam voluptatem quia voluptas sit aspernatur aut odit aut fugit, sed quia consequuntur magni dolores eos qui ratione voluptatem sequi nesciunt. Neque porro quisquam</p>
  </div>
  <div class="btn-grey abs">READ MORE</div>
</section>

<section class="products abs">
  <h2 class="section-title abs">OUR PRODUCTS</h2>
  <div class="dash-line abs"></div>
  <div class="product abs" style="left:93px">
    <div class="diamond"><svg width="40" height="40" viewBox="0 0 40 40" fill="none" stroke="#fff" stroke-width="2"><rect x="9" y="6" width="22" height="20"/><line x1="20" y1="6" x2="20" y2="26"/><line x1="9" y1="16" x2="31" y2="16"/><line x1="6" y1="30" x2="34" y2="30"/><line x1="10" y1="30" x2="10" y2="36"/><line x1="16" y1="30" x2="16" y2="36"/><line x1="24" y1="30" x2="24" y2="36"/><line x1="30" y1="30" x2="30" y2="36"/></svg></div>
    <h3>RESIDENTIAL</h3>
    <p>Lorem ipsum dolor sit amet, consectetur adipiscing elit, sed do eiusmod tempor incididunt ut labore et dolore magna aliqua. Ut enim ad minim veniam</p>
    <a>READ MORE</a>
  </div>
  <div class="product abs" style="left:443px">
    <div class="diamond"><svg width="40" height="40" viewBox="0 0 40 40" fill="none" stroke="#fff" stroke-width="2"><rect x="8" y="8" width="24" height="26"/><path d="M8 8l7 4v26l-7-4z" fill="#fff"/><path d="M32 8l-7 4v26l7-4z" fill="#fff"/></svg></div>
    <h3>COMMERCIAL</h3>
    <p>Lorem ipsum dolor sit amet, consectetur adipiscing elit, sed do eiusmod tempor incididunt ut labore et dolore magna aliqua. Ut enim ad minim veniam</p>
    <a>READ MORE</a>
  </div>
  <div class="product abs" style="left:808px">
    <div class="diamond"><svg width="40" height="40" viewBox="0 0 40 40" fill="none" stroke="#fff" stroke-width="2"><circle cx="20" cy="20" r="17"/><circle cx="20" cy="10" r="3"/><line x1="18" y1="13" x2="11" y2="32"/><line x1="22" y1="13" x2="29" y2="32"/><path d="M13 24q7 4 14 0"/></svg></div>
    <h3>ARCHITECTURAL</h3>
    <p>Lorem ipsum dolor sit amet, consectetur adipiscing elit, sed do eiusmod tempor incididunt ut labore et dolore magna aliqua. Ut enim ad minim veniam</p>
    <a>READ MORE</a>
  </div>
</section>

<section class="gallery">
  <h2 class="section-title abs">PROJECT GALLERY</h2>
  <div class="tile" style="left:100px;top:1845px;width:313px;height:155px;background:linear-gradient(180deg,#7a5a45,#b98a5c 70%,#8d5e38)" role="img" aria-label="Bright living room with timber floor and white windows"></div>
  <div class="tile" style="left:100px;top:2068px;width:313px;height:227px;background:linear-gradient(180deg,#6fa6d6,#3d5f84 60%,#2a4a6a)" role="img" aria-label="Modern white house with pool at twilight"></div>
  <div class="tile" style="left:427px;top:1845px;width:386px;height:211px;background:linear-gradient(180deg,#d8e6c8,#b6c9a0)" role="img" aria-label="Interior room with large glazed wall">
    <div class="tile-caption">SED UT PERSPICIATIS UNDE<br>OMNIS ISTE NATUS<span style="font-size:28px;line-height:34px">+</span></div>
  </div>
  <div class="tile" style="left:427px;top:2126px;width:386px;height:169px;background:linear-gradient(180deg,#eef0f2,#c9ced3)" role="img" aria-label="Empty white loft with black-framed windows"></div>
  <div class="tile" style="left:828px;top:1845px;width:270px;height:153px;background:linear-gradient(135deg,#9cc3e3,#b3714e 55%,#5b6c7a)" role="img" aria-label="Office building with red cladding and glass facade"></div>
  <div class="tile" style="left:828px;top:2006px;width:270px;height:289px;background:linear-gradient(180deg,#a9cbe8,#e2e8ec 45%,#6d8a4f 90%)" role="img" aria-label="White office building with rows of windows and a tree"></div>
</section>

<section class="testimonials abs" role="img" aria-label="Dimmed interior with floor-to-ceiling windows">
  <h2 class="section-title abs">TESTIMONIALS</h2>
  <div class="rule abs"></div>
  <p class="quote abs">“ Sed ut perspiciatis unde omnis iste natus error sit voluptatem accusantium doloremque laudantium, totam rem aperiam, eaque ipsa quae ab illo inventore veritatis et quasi architecto beatae vitae dicta sunt explicabo. Nemo enim ipsam voluptatem quia voluptas sit aspernatur aut odit aut fugit, sed quia consequuntur magni dolores eos qui ratione voluptatem ”</p>
  <p class="author abs">Mara Linden - Keel Harbor</p>
  <div class="dots abs"><i></i><i></i><i></i></div>
</section>

<footer class="site-footer abs">
  <div class="foot-col abs" style="left:97px">
    <h4>Contact Us</h4>
    <div class="foot-row"><svg width="12" height="16" viewBox="0 0 12 16"><path d="M6 0a6 6 0 0 0-6 6c0 4.5 6 10 6 10s6-5.5 6-10a6 6 0 0 0-6-6zm0 8.5A2.5 2.5 0 1 1 6 3.5a2.5 2.5 0 0 1 0 5z" fill="#666"/></svg><div>Keel Harbor<br>12 Quay Lane, Port Alder</div></div>
    <div class="foot-row"><svg width="14" height="14" viewBox="0 0 24 24"><path fill="#666" d="M6.6 10.8a15 15 0 0 0 6.6 6.6l2.2-2.2c.3-.3.7-.4 1-.2 1.1.4 2.3.6 3.6.6.6 0 1 .4 1 1V20c0 .6-.4 1-1 1A17 17 0 0 1 3 4c0-.6.4-1 1-1h3.5c.6 0 1 .4 1 1 0 1.3.2 2.5.6 3.6.1.3 0 .7-.2 1z"/></svg><div>Phone: (555) 014-2290</div></div>
    <div class="foot-row"><svg width="14" height="12" viewBox="0 0 14 12"><rect width="14" height="12" fill="#666"/><path d="M0 0l7 6 7-6" stroke="#f1f1f1" fill="none"/></svg><div>Email: info@keelharbor.example</div></div>
  </div>
  <div class="foot-col abs" style="left:412px">
    <h4>Sign up for newsletter</h4>
    <p style="width:250px;font-size:11px;line-height:18px">Excepteur sint occaecat cupidatat non proident, sunt in culpa qui officia deserunt</p>
    <div class="newsletter-input">Enter email</div>
    <div class="btn-signup btn-green">SIGN UP</div>
  </div>
  <div class="foot-col abs" style="left:753px">
    <h4>Quick Links</h4>
    <ul class="links" style="font-size:11px">
      <li>Home</li><li>About Us</li><li>Services</li><li>Projects</li><li>Fabricators</li><li>Contact Us</li>
    </ul>
  </div>
  <div class="foot-brand abs"><span class="brand-mark" style="width:24px;height:24px"></span><span class="brand-name">KEEL HARBOR</span></div>
</footer>
<div class="socials abs"><i></i><i></i><i></i><i></i></div>
<div class="copyright abs">©2017 Keel Harbor. All Rights Reserved.</div>

</body>
</html>
```